Harbor HVAC Contractors - Ductless Mini-Split Ad Creative Brief 4 cp ad images

Our Offers (Must Be Clearly Visible in the Design)
100% Satisfaction Guarantee
"We guarantee to keep you cool, or your money back! If you're not happy after we’ve had a chance to fix it, we’ll refund you!"

5-Year Labor Warranty
"That’s right – a 5-year labor warranty! No maintenance agreement required, just clean your filters each month!"

Chill-Wave Season 2026
"LIMITED-TIME OFFER: Get $999 off any ductless mini-split installation!"

Transparent Pricing
"What you see is what you pay—NO hidden fees!"

Ad Design Guidelines
Primary Focus: Ductless Mini-Split A/C Systems ONLY
Color Scheme: Must incorporate Harbor HVAC Contractors' main colors with a hint of yellow to catch attention.
Look at truck wrap to get a feel for the border of ad image creative
Branding Elements: Include Harbor HVAC logo prominently.
Contact Details: Display phone number clearly.
Trust Builders: Feature Chatterpage & Zintrova review elements to enhance credibility.
Visibility: The offers must be clear and readable but not overcrowded. Prioritize readability and clean design.
Final Notes
Ensure the design is high-converting and visually engaging while maintaining a professional, premium feel.
The ad creatives will be used for ductless mini-split A/C systems only—this must be clear in the design messaging.
Feel Free to use your expertise and experience to make this better
Thank you 555-203-7148

```html
<!DOCTYPE html>
<html lang="en">
<head>
<meta charset="utf-8">
<title>Harbor HVAC Contractors – Ductless Mini-Split Ad</title>
<link href="https://fonts.googleapis.com/css2?family=Montserrat:ital,wght@0,500;0,700;0,800;0,900;1,800;1,900&family=Racing+Sans+One&family=Roboto+Mono:wght@700&family=Roboto:wght@400;500;700&display=swap" rel="stylesheet">
<style>
:root{
  --navy:#0a2a6b;
  --navy-deep:#061a4a;
  --blue:#1552b0;
  --blue-mid:#1f62c4;
  --red:#c4161c;
  --red-dark:#7d0a0e;
  --orange:#ff6a13;
  --yellow:#fff200;
  --white:#ffffff;
  --ink:#111827;
  --grey:#c9ccd2;
}
*{box-sizing:border-box;margin:0;padding:0}
html,body{width:970px;height:1200px;overflow:hidden;background:var(--navy)}
.ad{position:relative;width:970px;height:1200px;overflow:hidden;
  background:linear-gradient(160deg,#2f6fd0 0%,#1650ae 35%,#0f3f94 65%,#0a2f77 100%);
  font-family:"Montserrat",sans-serif;color:var(--white)}
.backdrop{position:absolute;inset:0;
  background:radial-gradient(ellipse at 70% 60%,rgba(120,160,220,.35),transparent 60%),
             radial-gradient(ellipse at 20% 80%,rgba(10,30,80,.4),transparent 60%)}
.unit-photo{position:absolute;right:0;top:0;width:260px;height:380px;
  background:linear-gradient(200deg,#f1f3f6 0%,#cfd6e0 40%,rgba(80,120,190,.4) 75%,transparent 100%)}
.brand-panel{position:absolute;left:0;top:0;width:345px;height:205px}
.brand-panel svg{position:absolute;inset:0}
.brand-name{position:absolute;left:22px;top:70px;width:270px;display:flex;align-items:center;gap:12px;
  font-weight:800;font-size:25px;line-height:1.05;color:var(--navy)}
.brand-dot{flex:none;width:44px;height:44px;border-radius:50%;background:var(--red)}
.headline{position:absolute;left:352px;top:22px;font-style:italic;font-weight:900;line-height:1}
.headline .lead{font-size:44px;margin-left:8px}
.headline .big{display:block;font-size:74px;color:var(--yellow);letter-spacing:-1px;margin-top:2px}
.headline .sub{display:block;font-size:28px;margin-top:4px}
.photo-circle{position:absolute;width:136px;height:136px;border-radius:50%;border:6px solid var(--white);
  box-shadow:0 4px 10px rgba(0,0,0,.35)}
.photo-circle::after{content:"";position:absolute;left:10px;right:10px;bottom:-30px;height:10px;border-radius:50%;
  background:rgba(0,0,0,.35);filter:blur(3px)}
.offer-banner{position:absolute;height:31px;display:flex;align-items:center}
.offer-banner .tag{height:31px;padding:0 16px;display:flex;align-items:center;border-radius:4px;
  background:linear-gradient(#e3262c,#9c0f14);border-top:2px solid #ff5a5a;
  font-family:"Racing Sans One",sans-serif;font-style:italic;font-size:21px;letter-spacing:.5px;color:#fff;white-space:nowrap}
.offer-banner .chev{width:29px;height:31px;background:var(--orange);border-radius:4px;display:flex;align-items:center;justify-content:center}
.offer-text{position:absolute;font-family:"Roboto Mono",monospace;font-weight:700;font-size:16.5px;line-height:1.3;
  text-shadow:0 1px 2px rgba(0,0,0,.4);white-space:nowrap}
.offer-text.right{text-align:right}
.reviews-title{position:absolute;left:175px;top:730px;font-weight:800;font-style:italic;font-size:25px}
.rating{position:absolute;display:flex;align-items:center;gap:10px}
.rating .mark{flex:none;width:40px;height:40px;border-radius:50%;background:var(--white)}
.rating .name{font-weight:800;font-size:16px;color:var(--white);white-space:nowrap}
.rating .stars{color:var(--yellow);font-size:24px;line-height:1;letter-spacing:1px}
.rating .score{font-weight:700;font-size:19px;white-space:nowrap}
.shot{position:absolute;font-family:"Roboto",sans-serif;box-shadow:0 4px 14px rgba(0,0,0,.5);overflow:hidden}
.shot-light{left:47px;top:846px;width:254px;height:212px;background:#f2f3f5;color:var(--ink);font-size:5px;border:2px solid #fff}
.shot-light .cover{height:20px;background:linear-gradient(90deg,#1b2a55,#8aa0c8)}
.shot-light .head{padding:4px 6px;display:flex;gap:6px;align-items:center;background:#fff}
.shot-light .head .av{width:22px;height:22px;border-radius:50%;background:var(--red);margin-top:-12px;border:2px solid #fff}
.shot-light .head b{font-size:7px}
.shot-light .tabs{background:#fff;padding:3px 6px;border-top:1px solid #ddd;display:flex;gap:8px;color:#555}
.shot-light .card{background:#fff;margin:5px 35px 0;padding:4px;border-radius:2px}
.shot-light .card b{font-size:5.5px}
.shot-light .card p{margin-top:2px;color:#333;line-height:1.3}
.shot-dark{left:361px;top:846px;width:295px;height:186px;background:#1f1f22;color:#e4e4e4;font-size:5px;padding:10px 12px}
.shot-dark .title{font-size:10px;color:#e8e8e8}
.shot-dark .addr{color:#999;margin-top:1px}
.shot-dark .btn{position:absolute;right:14px;top:12px;background:#2b5bb7;color:#fff;padding:2px 5px;border-radius:2px}
.shot-dark .score{font-size:11px;margin-top:7px;display:flex;align-items:center;gap:4px}
.shot-dark .score .st{color:#f5b400;font-size:9px}
.chips{display:flex;gap:4px;margin-top:5px}
.chips span{border:1px solid #555;border-radius:8px;padding:2px 5px;color:#ccc}
.chips .on{background:#7aa2f7;color:#102;border-color:#7aa2f7}
.shot-dark .rev{border-top:1px solid #333;margin-top:9px;padding-top:7px;line-height:1.35}
.shot-dark .rev .who{display:flex;gap:4px;align-items:center}
.shot-dark .rev .who i{width:10px;height:10px;border-radius:50%;background:#8a6a4a;display:block}
.shot-dark .muted{color:#8aa2d8}
.watch{position:absolute;left:720px;top:930px;width:230px;text-align:center}
.watch h3{font-weight:800;font-style:italic;font-size:18px}
.socials{display:flex;justify-content:center;gap:10px;margin:10px 0 8px}
.socials span{display:flex;align-items:center;gap:4px;font-weight:800;font-size:11px}
.socials i{width:16px;height:16px;border-radius:50%;background:var(--red);display:block;border:2px solid #fff}
.watch .handle{font-weight:800;font-style:italic;font-size:19px;margin-left:-40px;margin-right:-40px}
.divider{position:absolute;left:0;top:1100px;width:970px;height:8px;background:linear-gradient(#e2e4e8,#a9aeb6)}
.footer{position:absolute;left:0;top:1108px;width:970px;height:92px;
  background:linear-gradient(90deg,#06164a,#0b2a78 50%,#06164a)}
.book{position:absolute;left:32px;top:21px;display:flex;gap:4px}
.book .label{background:var(--yellow);color:#000;height:44px;width:203px;border-radius:6px;display:flex;align-items:center;justify-content:center;
  font-weight:900;font-style:italic;font-size:27px;letter-spacing:-1px;white-space:nowrap}
.book .arrow{width:40px;height:44px;border-radius:4px;background:var(--orange);display:flex;align-items:center;justify-content:center}
.contact{position:absolute;top:22px;display:flex;align-items:center;gap:14px}
.contact .small{font-weight:800;font-size:12px;color:var(--yellow)}
.contact .big{font-weight:900;font-size:23px;color:var(--yellow);line-height:1.1;white-space:nowrap}
</style>
</head>
<body>
<main class="ad">
  <div class="backdrop" role="img" aria-label="Photo backdrop of a technician servicing an outdoor unit beside a stone wall, tinted blue"></div>
  <div class="unit-photo" role="img" aria-label="Photo of stacked outdoor ductless mini-split condenser units"></div>

  <header class="brand-panel">
    <svg width="345" height="205" viewBox="0 0 345 205" aria-hidden="true">
      <path d="M0 0 H325 Q300 120 240 205 H0 Z" fill="#c4161c"/>
      <path d="M0 0 H312 Q288 118 226 205 H0 Z" fill="#ffffff"/>
    </svg>
    <div class="brand-name"><span class="brand-dot"></span><span>Harbor HVAC Contractors</span></div>
  </header>

  <h1 class="headline">
    <span class="lead">A GREAT</span>
    <span class="big">EXPERIENCE</span>
    <span class="sub">FROM PEOPLE YOU KNOW</span>
  </h1>

  <!-- Offer 1 -->
  <div class="photo-circle" style="left:62px;top:226px;background:linear-gradient(150deg,#c7ccd3,#6b7d96 60%,#3a4a63)" role="img" aria-label="Photo of a customer with a technician outside a home"></div>
  <div class="offer-banner" style="left:195px;top:228px">
    <span class="chev"><svg width="14" height="18" viewBox="0 0 14 18"><path d="M11 2 L4 9 L11 16" stroke="#fff" stroke-width="3.5" fill="none"/></svg></span>
    <span class="tag" style="width:418px">100% SATISFACTION GUARANTEE</span>
  </div>
  <p class="offer-text" style="left:215px;top:266px">“We guarantee to keep you cool, or your<br>money back! If you're not  happy after<br>we've had a chance to fix it, we'll refund you!"</p>

  <!-- Offer 2 -->
  <div class="photo-circle" style="left:766px;top:347px;background:linear-gradient(160deg,#dfe3e8,#9aa6b5 55%,#3b4556)" role="img" aria-label="Photo of a team standing beside installed mini-split units in snow"></div>
  <div class="offer-banner" style="left:365px;top:366px">
    <span class="tag" style="width:356px">5-YEAR LABOR WARRANTY</span>
    <span class="chev"><svg width="14" height="18" viewBox="0 0 14 18"><path d="M3 2 L10 9 L3 16" stroke="#fff" stroke-width="3.5" fill="none"/></svg></span>
  </div>
  <p class="offer-text right" style="right:246px;top:400px">“That's right – a 5-year labor warranty!<br>No maintenance agreement required,<br>just clean your filters each month!"</p>

  <!-- Offer 3 -->
  <div class="photo-circle" style="left:62px;top:476px;background:linear-gradient(140deg,#e6e2dc,#8ea0b8 55%,#3d5a8a)" role="img" aria-label="Photo of a smiling technician giving a thumbs up beside a mini-split"></div>
  <div class="offer-banner" style="left:207px;top:496px">
    <span class="chev"><svg width="14" height="18" viewBox="0 0 14 18"><path d="M11 2 L4 9 L11 16" stroke="#fff" stroke-width="3.5" fill="none"/></svg></span>
    <span class="tag" style="width:350px">CHILL-WAVE SEASON 2026</span>
  </div>
  <p class="offer-text" style="left:237px;top:534px;font-size:17.5px;line-height:1.5">“LIMITED-TIME OFFER: Get $999<br>off any ductless mini-split installation!"</p>

  <!-- Offer 4 -->
  <div class="photo-circle" style="left:766px;top:588px;background:linear-gradient(150deg,#a48c74,#6f6257 50%,#2c3e5c)" role="img" aria-label="Photo of a technician working on an outdoor unit by a stone wall"></div>
  <div class="offer-banner" style="left:412px;top:604px">
    <span class="tag" style="width:316px">TRANSPARENT PRICING</span>
    <span class="chev"><svg width="14" height="18" viewBox="0 0 14 18"><path d="M3 2 L10 9 L3 16" stroke="#fff" stroke-width="3.5" fill="none"/></svg></span>
  </div>
  <p class="offer-text right" style="right:241px;top:642px;font-size:18px;line-height:1.45">“What you see is what you pay<br>NO hidden fees!"</p>

  <!-- Reviews -->
  <h2 class="reviews-title">Chatterpage &amp; Zintrova review</h2>

  <div class="rating" style="left:60px;top:778px">
    <span class="mark"></span>
    <span class="name">Chatterpage</span>
    <div><div class="stars">★★★★★</div><div class="score">5.0 RATING</div></div>
  </div>
  <div class="rating" style="left:405px;top:785px">
    <span class="mark"></span>
    <span class="name">Zintrova</span>
    <div><div class="stars">★★★★★</div><div class="score">5.0 RATING</div></div>
  </div>

  <section class="shot shot-light">
    <div class="cover"></div>
    <div class="head"><span class="av"></span><div><b>Harbor HVAC Contractors</b><br>128 likes · 134 followers</div></div>
    <div class="tabs"><span>Home</span><span>About</span><span>Posts</span><span>Photos</span><span>Videos</span></div>
    <div class="card"><b>Not yet rated (3 reviews)</b></div>
    <div class="card"><b>Mara Ellison recommends Harbor HVAC Contractors.</b>
      <p>Highly recommend Rob and his team. They were quick, honest and easy to work with from start to finish.</p></div>
    <div class="card"><b>Colleen Rusk recommends Harbor HVAC Contractors.</b>
      <p>Great experience from quote to install. Everything was explained clearly and the work was tidy.</p></div>
  </section>

  <section class="shot shot-dark">
    <div class="title">Harbor Hvac Contractors LLC</div>
    <div class="addr">48 Alder Ln Suite 4, Ridgeview, CO, United States</div>
    <span class="btn">Write a review</span>
    <div class="score">5.0 <span class="st">★★★★★</span> <span style="font-size:5px;color:#999">25 reviews</span></div>
    <div style="margin-top:5px">Topics that people often talk about</div>
    <div class="chips"><span class="on">All</span><span>install 4</span><span>mini-split 3</span><span>repair 3</span><span>quote 3</span><span>+6</span></div>
    <div style="margin-top:5px">Sort by</div>
    <div class="chips"><span class="on">Most relevant</span><span>Latest</span><span>Highest</span><span>Lowest</span></div>
    <div class="rev">
      <div class="who"><i></i><div><b>Dana Whitlow</b><br>3 reviews</div></div>
      <div><span style="color:#f5b400">★★★★★</span> a month ago</div>
      <div>Harbor came to my house to fix a leak in my laundry room. They were able to make a quick service call when I needed it and did a great job. They were fast... <span class="muted">More</span></div>
      <div class="muted">Translated by Zintrova · View original (English)</div>
      <div>Thanks</div>
    </div>
  </section>

  <div class="watch">
    <h3>Watc Us Work</h3>
    <div class="socials">
      <span><i></i>Chatterpage</span><span><i></i>Vidstream</span><span><i></i>Clipto</span>
    </div>
    <div class="handle">@harborhvaccontractor</div>
  </div>

  <div class="divider"></div>
  <footer class="footer">
    <div class="book">
      <span class="label">BOOK NOW!</span>
      <span class="arrow"><svg width="20" height="26" viewBox="0 0 20 26"><path d="M5 3 L15 13 L5 23" stroke="#fff" stroke-width="4.5" fill="none"/></svg></span>
    </div>
    <div class="contact" style="left:310px">
      <svg width="38" height="38" viewBox="0 0 38 38" aria-hidden="true">
        <path d="M9 5 L15 5 L17 13 L13 16 Q16 23 22 26 L25 22 L33 24 L33 30 Q33 34 28 34 Q13 32 5 14 Q4 5 9 5 Z" fill="none" stroke="#fff" stroke-width="2.6"/>
        <path d="M22 6 Q30 8 32 16 M22 11 Q26 12 27 16" stroke="#fff" stroke-width="2.4" fill="none"/>
      </svg>
      <div><div class="small">Call to find out more</div><div class="big">555-203-7148</div></div>
    </div>
    <div class="contact" style="left:553px">
      <svg width="40" height="40" viewBox="0 0 40 40" aria-hidden="true" fill="none" stroke="#fff" stroke-width="2.4">
        <circle cx="19" cy="19" r="15"/><ellipse cx="19" cy="19" rx="6.5" ry="15"/><path d="M4 19 H34 M7 11 H31 M7 27 H31"/>
        <path d="M26 25 L37 30 L32 32 L35 37 L33 38 L30 33 L27 36 Z" fill="#fff"/>
      </svg>
      <div><div class="small">Visit Our Website</div><div class="big">HARBORHVACPROS.COM</div></div>
    </div>
  </footer>
</main>
</body>
</html>
```